Downloadable PDF "Brochure?"

We have a Free download we will provide in exchange for an email address on our new Trailmark website. The website at www.venturetrailmark-example.com is in development and will look nothing like what it currently does, but you can go there and get a sense of what Trailmark is from the text on the website. (see the attached image 'site design' for the new redesigned website for aesthetics).

We are looking for a nice design for the document, that will represent the mostly text document well. We are not actually looking to print these at a printer so they don't have to be print ready. I went ahead and included the logo and colors and fonts file again just for reference.

Target Market(s)

Business Owners / Decision Makers

Requirements
Must have
• See attached document 'trailmark freebie' for text to be utilized in the finished deliverable.
• See the attached image 'Site Design' for the website aesthetic.

```html
<!DOCTYPE html>
<html lang="en">
<head>
<meta charset="utf-8">
<title>Trailmark – 10 Questions To Choose The Best Technology Advisor</title>
<link href="https://fonts.googleapis.com/css2?family=Cinzel:wght@400&family=EB+Garamond:wght@400&display=swap" rel="stylesheet">
<style>
:root{
  --slate:#3b4a52;
  --copper:#c97a4a;
  --ink:#4a4a4a;
  --paper:#ffffff;
  --backdrop:#e4e4e4;
}
*{margin:0;padding:0;box-sizing:border-box}
html,body{width:965px;height:1200px;overflow:hidden;background:var(--backdrop)}
.spread{position:relative;width:965px;height:1200px}
.page{position:absolute;width:283px;height:366px;background:var(--paper);overflow:hidden}
.bar-dark{position:absolute;left:0;top:0;width:26px;background:var(--slate)}
.bar-copper{position:absolute;left:26px;top:0;width:7px;height:318px;background:var(--copper)}
.num{position:absolute;left:0;width:40px;height:38px;background:var(--slate);color:#fff;
  font-family:"EB Garamond",serif;font-weight:400;font-size:36px;line-height:38px;text-align:center;letter-spacing:-1px}
.q{position:absolute;left:70px;width:192px;font-family:"Cinzel",serif;font-weight:400;font-size:6.6px;line-height:8.6px;
  color:var(--copper);letter-spacing:.3px}
.a{position:absolute;left:70px;width:184px;font-family:"EB Garamond",serif;font-size:5.4px;line-height:11px;color:var(--ink)}
.footer-band{position:absolute;bottom:0;left:90px;width:178px;height:21px;background:var(--copper);
  border-radius:12px 12px 0 0;color:#fff;font-family:"Cinzel",serif;font-size:7px;
  letter-spacing:1.6px;line-height:22px;text-align:center}
.mini-mark{position:absolute;left:14px;bottom:14px;width:40px;text-align:center}
.mini-mark .dot{display:block;width:12px;height:12px;border-radius:50%;background:var(--slate);margin:0 auto 2px}
.mini-mark .name{font-family:"Cinzel",serif;font-size:4.6px;color:var(--ink);letter-spacing:.3px}
.cover-photo{position:absolute;left:0;top:0;width:283px;height:250px;
  background:linear-gradient(180deg,#9a9a98 0%,#b4b4b2 45%,#d9dad9 75%,#ffffff 100%)}
.cover-badge{position:absolute;left:39px;top:54px;width:33px;height:30px;background:var(--copper);color:#fff;
  font-family:"EB Garamond",serif;font-size:28px;line-height:31px;text-align:center}
.cover-title{position:absolute;left:38px;top:94px;font-family:"Cinzel",serif;font-weight:400;font-size:11px;line-height:13.8px;color:#fff;letter-spacing:.5px}
.brand{position:absolute;left:0;width:283px;text-align:center}
.brand .dot{display:block;width:36px;height:36px;border-radius:50%;background:var(--slate);margin:0 auto 8px}
.brand .name{font-family:"Cinzel",serif;font-size:10px;letter-spacing:.8px;color:var(--ink)}
.cover-intro{position:absolute;left:36px;top:299px;width:211px;text-align:center;font-family:"EB Garamond",serif;
  font-size:4.9px;line-height:6.6px;color:var(--ink)}
.contact{position:absolute;top:303px;font-family:"EB Garamond",serif;font-size:5.2px;line-height:11px;color:var(--ink)}
.contact svg{vertical-align:-1px;margin-right:4px}
</style>
</head>
<body>
<main class="spread">

  <section class="page" style="left:45px;top:33px">
    <div class="cover-photo" role="img" aria-label="Photo of a businessman standing at a round opening in a concrete wall overlooking a city skyline"></div>
    <div class="cover-badge">10</div>
    <h1 class="cover-title">Questions To<br>Choose The<br>Best<br>Technology<br>Advisor</h1>
    <div class="brand" style="top:226px"><span class="dot"></span><div class="name">TRAILMARK</div></div>
    <p class="cover-intro">When you choose a technology advisor whether it be a Managed Service Provider, fractional CIO or a full-time CIO you need to make sure that they understand business just as much as they understand technology. Some of the biggest complaints about the IT department are that they just don't "Get it". The questions below should help you determine whether or not they have a technology mindset or a business mindset.</p>
    <div class="footer-band">WWW.TRAILMARK-EXAMPLE.COM</div>
  </section>

  <section class="page" style="left:344px;top:33px">
    <div class="bar-dark" style="height:247px"></div><div class="bar-copper"></div>
    <div class="num" style="top:30px">01</div>
    <h2 class="q" style="top:30px">What is scalability? How important is it from a technology perspective on a scale of 1-&gt;10 with 10 being the highest? What all does scalability impact?</h2>
    <p class="a" style="top:78px">This question is designed to get a reading on the person's mindset. A typical technology-minded response would be something describing the ability of systems or software to scale by adding additional resources. When working from a business point of view, however, you want to see it defined as the ability for the organization to support increased volume without sacrificing margins. The importance of this concept cannot be overstated and should be a 9 or 10 in terms of ranking. Regarding impact, you want to see not just an understanding of having to spend money two or three times for a different solution to the same problem, but an acknowledgment of the 'total' cost, including adoption fatigue, the opportunity cost of change, and the competitive disadvantage it creates. For concepts of business scalability refer to 'Growing Wide' by Dana Whitlock.</p>
    <div class="mini-mark"><span class="dot"></span><span class="name">TRAILMARK</span></div>
    <div class="footer-band">WWW.TRAILMARK-EXAMPLE.COM</div>
  </section>

  <section class="page" style="left:637px;top:33px">
    <div class="bar-dark" style="height:185px"></div><div class="bar-copper"></div>
    <div class="num" style="top:30px">02</div>
    <h2 class="q" style="top:30px">Provide an example where you solved a problem without the use of technology.</h2>
    <p class="a" style="top:55px">Often technology-minded individuals become so wrapped up in the solutions themselves they fail to realize a policy or process change is far more effective and simple than making changes to existing or introducing new technology. Asking for a specific example here should demonstrate the ability to think from a business mindset. For specific examples reference 'The Ember Project' by Lane, Orr, and Pike.</p>
    <div class="num" style="top:147px">03</div>
    <h2 class="q" style="top:149px">How do you go about prioritizing solutions in order of importance for implementation / adoption?</h2>
    <p class="a" style="top:183px">Answers here should include reference to some form of discovery process or a thorough evaluation at the operations level. One of the key skill sets for someone approaching technology from a business point of view is mapping solutions and their respective importance to business outcomes and (often more importantly) eliminating bottlenecks while respecting that some implementations must necessarily come before others to be viable. For reference on the Theory of Constraints see 'The Aim' by Ruben Castell.</p>
    <div class="mini-mark"><span class="dot"></span><span class="name">TRAILMARK</span></div>
    <div class="footer-band">WWW.TRAILMARK-EXAMPLE.COM</div>
  </section>

  <section class="page" style="left:45px;top:414px">
    <div class="bar-dark" style="height:246px"></div><div class="bar-copper"></div>
    <div class="num" style="top:28px">04</div>
    <h2 class="q" style="top:29px">What is Information Technology Debt?</h2>
    <p class="a" style="top:45px">Stated simply, 'IT Debt' is a measurement of the out-of-date, incomplete or yet-to-be-defined technology changes. Debt occurs for a number of reasons, including lack of qualified personnel to implement the needed solutions (or recognize the problem in the first place); historical spending haunting the organization "we spent money on something like this before and look what it got us"; Fire-fighting (addressing issues purely reactively in a downward spiral leaving no time for fixing the real underlying problem); or most commonly, the budget being already allocated to other company endeavors that seem immediately more pressing. By recognizing what IT Debt is, the individual demonstrates an acknowledgment of how impactful it can be when neglected and not brought to the forefront of business planning sessions.</p>
    <div class="num" style="top:194px">05</div>
    <h2 class="q" style="top:198px">Provide an example where you argued against implementing a technology solution and why.</h2>
    <p class="a" style="top:230px">Despite it being seemingly obvious, using 'outside of budget' is not a good answer. Business-minded technology advisors should be intimately aware of how well a proposed solution will integrate into the existing company ecosystem (software tools already present, workflow, and processes), if it drives the company toward reducing/eliminating a bottleneck (and thereby creates more leverage), and if it fits the company's culture. If any of these are a no, the solution should be carefully examined for what it really offers the organization. If yes, the budget should be evaluated as a cost-benefit analysis, not a flat number 'not to exceed'.</p>
    <div class="mini-mark"><span class="dot"></span><span class="name">TRAILMARK</span></div>
    <div class="footer-band">WWW.TRAILMARK-EXAMPLE.COM</div>
  </section>

  <section class="page" style="left:344px;top:414px">
    <div class="bar-dark" style="height:218px"></div><div class="bar-copper"></div>
    <div class="num" style="top:28px">06</div>
    <h2 class="q" style="top:29px">What is your ideal method for maintaining technology alignment for the company?</h2>
    <p class="a" style="top:54px">You want to see a specific process envisioned here. At the very least a recommendation to be involved in business planning meetings or retreats, and ideally a standing technology focused meeting with leadership present should be argued for. For technology to be truly in alignment, it must fit the needs of the organization, not the other way around. This needs to come from the top level, and it means a representative must be present in critical business strategy meetings to understand where the company is headed, what operational constraints they are encountering, and what their short-term goals are. For an outline of how this model has been the underlying key to success for several well-known companies reference 'Solid to Stellar' by Joel Carver.</p>
    <div class="num" style="top:180px">07</div>
    <h2 class="q" style="top:182px">How do you plan on measuring and monitoring the adoption success of a solution or project?</h2>
    <p class="a" style="top:218px">Technically minded individuals often look at the point of 'it's up and running and it all works', as where their responsibilities end. Someone with a business mindset should demonstrate that evaluating how well the solution has been adopted into the day to day workflow, and to what degree the solution has increased leverage or operational transparency are the true critical indicators of success. There should be a specific process of follow-up after implementation to flag adoption or workflow issues due to problems such as inadequate training, unforeseen incompatibilities (whether they be process or technology related), or simply resistance to change. These findings can then be brought back to leadership to evaluate how best to improve successful adoption going forward.</p>
    <div class="mini-mark"><span class="dot"></span><span class="name">TRAILMARK</span></div>
    <div class="footer-band">WWW.TRAILMARK-EXAMPLE.COM</div>
  </section>

  <section class="page" style="left:637px;top:414px">
    <div class="bar-dark" style="height:218px"></div><div class="bar-copper"></div>
    <div class="num" style="top:30px">08</div>
    <h2 class="q" style="top:32px">Provide an example where you had to balance customer and employee technology experience with security and compliance.</h2>
    <p class="a" style="top:65px">A critical role fulfilled by a technology advisor is being able to balance maintaining compliance and sound security practices with as painless of a technology experience as possible. They should be able to weigh the critical importance of protecting the organization from the negative public relations and liability of a security flaw while respecting a solution must be usable to be useful. Look for an example that demonstrates an understanding of both sides and strikes a balance without going to an extreme in either direction.</p>
    <div class="num" style="top:178px">09</div>
    <h2 class="q" style="top:179px">What would you do first, if you were selected as our advisor? Can you give me details on what your discovery or on-boarding process includes?</h2>
    <p class="a" style="top:222px">You are looking to make sure that they don't stop at the technology. There should be a higher focus on understanding what the company processes are and how the people inside the organization get work done. If they focus only on network, security, and disaster recovery assessments then they do not have a business mindset.</p>
    <div class="mini-mark"><span class="dot"></span><span class="name">TRAILMARK</span></div>
    <div class="footer-band">WWW.TRAILMARK-EXAMPLE.COM</div>
  </section>

  <section class="page" style="left:344px;top:799px">
    <div class="bar-dark" style="height:246px"></div><div class="bar-copper" style="height:335px"></div>
    <div class="num" style="top:30px">10</div>
    <h2 class="q" style="top:30px">Can you give me an example of a time you gave a suggestion for a solution and it was not taken? Describe the solution and why it was important to the organization. And why do you think they didn't implement it?</h2>
    <p class="a" style="top:90px">When they describe why they think the solution was important do they simply talk about risk reduction or uptime improvements without tying them back to an organizational goal or bottleneck. Being able to demonstrate actual business value is a critical skill for a technology advisor. For reference on technical excellence in service of business objectives rather than blindly servicing requirements see 'A Chair in the Room' by Mason Hale.</p>
    <div class="brand" style="top:240px;left:70px;width:90px;text-align:left">
      <span class="dot" style="width:28px;height:28px;margin:0 0 6px 20px"></span>
      <div class="name" style="font-size:9px">TRAILMARK</div>
    </div>
    <div class="contact" style="left:70px">Address, PO-Box 4410<br>Sample street,<br>suite 300, country</div>
    <div class="contact" style="left:138px">
      <div><svg width="6" height="6" viewBox="0 0 10 10"><path d="M2 1l2 2-1 1.5c.8 1.5 2 2.7 3.5 3.5L8 7l2 2-1.5 1C4 9.5.5 6 0 2.5z" fill="#c97a4a"/></svg>555-010-2200</div>
      <div><svg width="6" height="6" viewBox="0 0 10 10"><rect x="2" y="0" width="6" height="3" fill="#c97a4a"/><rect x="0" y="3.5" width="10" height="4" fill="#c97a4a"/><rect x="2" y="7" width="6" height="3" fill="none" stroke="#c97a4a"/></svg>555-010-2201</div>
      <div><svg width="6" height="5" viewBox="0 0 10 8"><rect width="10" height="8" fill="#c97a4a"/><path d="M0 0l5 4 5-4" stroke="#fff" fill="none"/></svg>hello@trailmark-example.com</div>
    </div>
    <div class="footer-band" style="left:60px">WWW.TRAILMARK-EXAMPLE.COM</div>
  </section>

</main>
</body>
</html>
```